Austrian finance und insurance broker needs business card design

We Need a serious looking Design for Business Card. we consult private and corporates customers in finance and insurance questions. the final design should express security and experience. We consult customers in questions of loans, Investments and insurance and have a wide range of Banks to offer. We compare several offers and select the best for our customers.

Target Market(s)

private and coporate customers with efforts in Money and insurance

Industry/Entity Type

Insurance Broker

Contact Information for Business Card

Bernhard Aigner
Geschäftsführer
staatl. geprüfter Vermögensberater und Versicherungsmakler
Tel: 0664 521 8409
office@der-brandl.at
www.der-brandl.at
Leopold Hainz Gasse 14
2183 Melkstetten
GISA Nr. 48270315 u. 51736048 (backside)

Font styles to use
Serif
Sans Serif

Requirements
Must have
• logo (designcrowd zip) and all Details
Nice to have
• makler logo design, maybe a 2 coloured Version is possible

```html
<!DOCTYPE html>
<html lang="de">
<head>
<meta charset="utf-8">
<title>Aigner Finanzpartner – Visitenkarte</title>
<link rel="stylesheet" href="https://fonts.googleapis.com/css2?family=Quicksand:wght@400;500;600;700&display=swap">
<style>
  :root {
    --stage: #2a2c30;
    --card-dark: #2b2b2d;
    --card-light: #f7f7f8;
    --brand-blue: #2f64c8;
    --text-light: #e9e9ea;
    --text-grey: #6f7074;
    --divider: #6a6b6f;
    --badge-red: #c8232c;
  }
  * { box-sizing: border-box; margin: 0; padding: 0; }
  html, body { width: 1200px; height: 900px; overflow: hidden; }
  body {
    background: var(--stage);
    font-family: "Quicksand", sans-serif;
    position: relative;
  }
  .card {
    position: absolute;
    top: 290px;
    width: 520px;
    height: 320px;
    border-radius: 22px;
    overflow: hidden;
    background: var(--card-dark);
    box-shadow: 0 10px 30px rgba(0,0,0,.45);
  }
  .card--front { left: 50px; }
  .card--back { left: 630px; }

  /* front */
  .front__header {
    position: absolute; left: 0; top: 0; width: 100%; height: 112px;
    background: var(--card-light);
  }
  .brand {
    position: absolute; left: 28px; top: 30px;
    display: flex; align-items: center; gap: 12px;
  }
  .brand__mark {
    width: 16px; height: 16px; border-radius: 50%;
    background: var(--brand-blue);
  }
  .brand__rule { width: 1px; height: 50px; background: var(--text-grey); }
  .brand__name {
    color: var(--brand-blue); font-weight: 700; font-size: 17px; line-height: 1.1;
  }
  .brand__tagline {
    color: var(--text-grey); font-weight: 500; font-size: 11px; margin-top: 4px;
  }
  .partner-badge {
    position: absolute; right: 40px; top: 24px;
    width: 60px; height: 60px; border-radius: 50%;
    background: var(--badge-red);
  }
  .person {
    position: absolute; left: 20px; top: 138px; width: 230px;
    text-align: right;
  }
  .person__name { color: var(--brand-blue); font-weight: 700; font-size: 22px; }
  .person__role { color: var(--text-light); font-size: 12px; font-weight: 500; margin-top: 2px; }
  .person__qualification { color: var(--brand-blue); font-size: 11.5px; font-weight: 500; margin-top: 6px; line-height: 1.35; }
  .person__address { color: var(--text-light); font-size: 12px; font-weight: 500; margin-top: 10px; line-height: 1.4; }
  .front__divider {
    position: absolute; left: 266px; top: 144px; width: 1px; height: 140px;
    background: var(--divider);
  }
  .contact {
    position: absolute; left: 284px; top: 150px;
    list-style: none;
  }
  .contact__item {
    display: flex; align-items: center; gap: 10px;
    color: var(--text-light); font-size: 13px; font-weight: 500;
    height: 28px;
  }
  .contact__icon { width: 12px; height: 12px; fill: var(--brand-blue); flex: none; }
  .contact__label { color: var(--brand-blue); font-weight: 700; }

  /* back */
  .back__lockup {
    position: absolute; left: 0; top: 122px; width: 100%;
    text-align: center;
  }
  .back__name { color: var(--brand-blue); font-weight: 700; font-size: 30px; }
  .back__tagline { color: #5c5d61; font-weight: 600; font-size: 20px; margin-top: 6px; }
</style>
</head>
<body>
  <section class="card card--front">
    <header class="front__header">
      <div class="brand">
        <span class="brand__mark"></span>
        <span class="brand__rule"></span>
        <div>
          <div class="brand__name">Aigner Finanzpartner GmbH</div>
          <div class="brand__tagline">Kredite, Anlagen, Absicherung</div>
        </div>
      </div>
      <div class="partner-badge" aria-hidden="true"></div>
    </header>

    <div class="person">
      <div class="person__name">Bernhard Aigner</div>
      <div class="person__role">Geschäftsführer</div>
      <div class="person__qualification">Staatl. geprüfter Vermögensberater<br>und Versicherungsmakler</div>
      <div class="person__address">Leopold Hainz Gasse 14<br>2183 Melkstetten</div>
    </div>

    <span class="front__divider"></span>

    <ul class="contact">
      <li class="contact__item">
        <svg class="contact__icon" viewBox="0 0 24 24"><path d="M6.6 10.8a15.2 15.2 0 0 0 6.6 6.6l2.2-2.2a1 1 0 0 1 1-.25 11.4 11.4 0 0 0 3.6.57 1 1 0 0 1 1 1V20a1 1 0 0 1-1 1A17 17 0 0 1 3 4a1 1 0 0 1 1-1h3.5a1 1 0 0 1 1 1c0 1.25.2 2.45.57 3.6a1 1 0 0 1-.25 1z"/></svg>
        0664 521 8409
      </li>
      <li class="contact__item">
        <svg class="contact__icon" viewBox="0 0 24 24"><path d="M2 5h20v14H2z M2 5l10 8 10-8" /></svg>
        office@der-brandl.at
      </li>
      <li class="contact__item">
        <svg class="contact__icon" viewBox="0 0 24 24"><circle cx="12" cy="12" r="10"/></svg>
        www.der-brandl.at
      </li>
      <li class="contact__item">
        <span class="contact__label">GISA Nr.</span> 48270315 u. 51736048
      </li>
    </ul>
  </section>

  <section class="card card--back">
    <div class="back__lockup">
      <div class="back__name">Aigner Finanzpartner GmbH</div>
      <div class="back__tagline">Kredite, Anlagen, Absicherung</div>
    </div>
  </section>
</body>
</html>
```